Bench Advertisement - We Buy Houses Design Needed

Need a catchy, simple but elegant design for bus benches to advertise our company.

We need our website, or phone number, and a smal description (1-2 bulletpoints of what we do and what we offer)

The tricky part is for the designer to fit everything and make the website name as part of the title and fitting everything so that people passing by on the street can see what we offer.

Our website is quickhomebuyerdesk.com - (916) 482-3091

Something simple but something that catches the eye of walking pedestrians, and drivers driving by the bench.

Our company buys houses, any condition, any situation, we buy houses for cash and close quickly. You can use this description to create a few bulletpoints however you like. Must follow dimensions in attachment.

Target Market(s)

People in foreclosure, about to lose their homes, people that need a quick cash sale of their property

Industry/Entity Type

Real Estate

Requirements
Must have
• catchy, website name, phone number, few brief bulletpoints about what we offer, colors that will catch peoples eye while walking or driving - advertisement will be placed on bus benches - visit our website to see the type of houses we buy - Also have more work for winner of design with possible bonuses
Nice to have
• Feel free to use description or images on our website - make sure the description is just bullet points and it fits with the overall theme / size of the advertisement - Bold bright colors - put yourself in their shoes (if you were going through financial difficulties and about to lose your house to foreclosure or auction, what would you want to see to pick up the phone and call us for a quick sale of your house?) (or if you have a house that you are having a problem with, problem renters, unkept/beat up house, what would make you want to call us and sell your house to us?)

```html
<!DOCTYPE html>
<html lang="en">
<head>
<meta charset="utf-8">
<title>Quick Home Buyer Desk – Bench Ad Variants</title>
<link rel="stylesheet" href="https://fonts.googleapis.com/css2?family=Archivo+Black&family=Montserrat:wght@800&family=Francois+One&family=Rubik:wght@900&display=swap">
<style>
  :root {
    --purple: #42409a;
    --orange: #fbb316;
    --ink: #231f20;
    --white: #ffffff;
  }
  * { box-sizing: border-box; margin: 0; padding: 0; }
  html, body { width: 1200px; height: 1200px; overflow: hidden; background: var(--white); }
  .board { position: relative; width: 1200px; height: 1200px; }

  .bench-ad {
    position: absolute;
    left: 197px;
    width: 810px;
    height: 231px;
    background: var(--bg);
    overflow: hidden;
    box-shadow: -3px -3px 5px rgba(0,0,0,.22);
  }
  .bench-ad--purple { top: 209px; --bg: var(--purple); --tab: var(--orange); --title: var(--purple); --tag: var(--white); --band: var(--orange); --site: var(--purple); --call: var(--orange); --bullet: var(--white); }
  .bench-ad--orange { top: 479px; --bg: var(--orange); --tab: var(--purple); --title: var(--white); --tag: var(--purple); --band: var(--purple); --site: var(--white); --call: var(--ink); --bullet: var(--purple); }
  .bench-ad--black  { top: 759px; --bg: var(--orange); --tab: var(--ink); --title: var(--white); --tag: var(--ink); --band: var(--ink); --site: var(--white); --call: var(--ink); --bullet: var(--ink); }

  .title-tab {
    position: absolute; left: 0; top: 20px; width: 325px; height: 101px;
    background: var(--tab); border-top-right-radius: 16px;
  }
  .title-word {
    position: absolute; left: 18px; top: 28px;
    font-family: "Archivo Black", sans-serif; font-size: 96px; line-height: 100px;
    color: var(--title); letter-spacing: -1px;
    transform: scaleX(.8); transform-origin: left top;
    white-space: nowrap;
  }
  .site-band {
    position: absolute; left: 0; top: 119px; width: 100%; height: 47px; background: var(--band);
  }
  .site-name {
    position: absolute; left: 20px; top: 108px;
    font-family: "Montserrat", sans-serif; font-weight: 800; font-size: 62px; line-height: 62px;
    color: var(--site); letter-spacing: 3px; white-space: nowrap;
  }
  .tagline {
    position: absolute; left: 346px; top: 26px; list-style: none;
    font-family: "Rubik", sans-serif; font-weight: 900; font-size: 24px; line-height: 29px;
    color: var(--tag);
  }
  .brand {
    position: absolute; left: 560px; top: 44px; width: 215px;
    display: flex; align-items: center; justify-content: center; gap: 8px;
    font-family: "Montserrat", sans-serif; font-weight: 800; font-size: 16px; line-height: 20px;
    color: var(--tag); text-align: left;
  }
  .brand-square { width: 28px; height: 28px; background: var(--tag); flex: none; }

  .call-line {
    position: absolute; left: 20px; right: 24px; top: 168px;
    display: flex; justify-content: space-between; white-space: nowrap;
    font-family: "Francois One", sans-serif; font-size: 30px; line-height: 32px;
    color: var(--call);
  }
  .no-obligation { position: relative; }
  .swoosh { position: absolute; left: -40px; bottom: -3px; width: 190px; height: 10px; }
  .swoosh path { stroke: var(--call); }

  .situations {
    position: absolute; left: 19px; right: 24px; top: 203px;
    display: flex; justify-content: space-between; list-style: none; white-space: nowrap;
    font-family: "Francois One", sans-serif; font-size: 15px; line-height: 16px;
    color: var(--bullet); letter-spacing: .3px;
  }
  .situations li { display: flex; align-items: center; gap: 8px; }
  .situations svg { width: 11px; height: 11px; fill: var(--bullet); }
</style>
</head>
<body>
<main class="board">

  <section class="bench-ad bench-ad--purple">
    <div class="title-tab"></div>
    <div class="title-word">QUICK</div>
    <div class="site-band"></div>
    <div class="site-name">homebuyerdesk.com</div>
    <ul class="tagline"><li>Sell for cash</li><li>Quick closure</li><li>Any condition</li></ul>
    <div class="brand"><span class="brand-square"></span><span>QUICK HOME BUYER DESK</span></div>
    <p class="call-line"><span>Call or Text Us Now for a <span class="no-obligation">No Obligation<svg class="swoosh" viewBox="0 0 190 10"><path d="M2 8 Q95 0 188 3" fill="none" stroke-width="1.5"/></svg></span> Offer</span><span>(916) 482-3091</span></p>
    <ul class="situations">
      <li><svg viewBox="0 0 11 11"><rect x="0" y="0" width="4.5" height="4.5"/><rect x="6.5" y="0" width="4.5" height="4.5"/><rect x="0" y="6.5" width="4.5" height="4.5"/><rect x="6.5" y="6.5" width="4.5" height="4.5"/></svg>Financial Difficulties</li>
      <li><svg viewBox="0 0 11 11"><rect x="0" y="0" width="4.5" height="4.5"/><rect x="6.5" y="0" width="4.5" height="4.5"/><rect x="0" y="6.5" width="4.5" height="4.5"/><rect x="6.5" y="6.5" width="4.5" height="4.5"/></svg>Foreclosure or Auction</li>
      <li><svg viewBox="0 0 11 11"><rect x="0" y="0" width="4.5" height="4.5"/><rect x="6.5" y="0" width="4.5" height="4.5"/><rect x="0" y="6.5" width="4.5" height="4.5"/><rect x="6.5" y="6.5" width="4.5" height="4.5"/></svg>Quick Sale</li>
      <li><svg viewBox="0 0 11 11"><rect x="0" y="0" width="4.5" height="4.5"/><rect x="6.5" y="0" width="4.5" height="4.5"/><rect x="0" y="6.5" width="4.5" height="4.5"/><rect x="6.5" y="6.5" width="4.5" height="4.5"/></svg>Problem Renters</li>
      <li><svg viewBox="0 0 11 11"><rect x="0" y="0" width="4.5" height="4.5"/><rect x="6.5" y="0" width="4.5" height="4.5"/><rect x="0" y="6.5" width="4.5" height="4.5"/><rect x="6.5" y="6.5" width="4.5" height="4.5"/></svg>Unkept/Beat Up House</li>
    </ul>
  </section>

  <section class="bench-ad bench-ad--orange">
    <div class="title-tab"></div>
    <div class="title-word">QUICK</div>
    <div class="site-band"></div>
    <div class="site-name">homebuyerdesk.com</div>
    <ul class="tagline"><li>Sell for cash</li><li>Quick closure</li><li>Any condition</li></ul>
    <div class="brand"><span class="brand-square"></span><span>QUICK HOME BUYER DESK</span></div>
    <p class="call-line"><span>Call or Text Us Now for a <span class="no-obligation">No Obligation<svg class="swoosh" viewBox="0 0 190 10"><path d="M2 8 Q95 0 188 3" fill="none" stroke-width="1.5"/></svg></span> Offer</span><span>(916) 482-3091</span></p>
    <ul class="situations">
      <li><svg viewBox="0 0 11 11"><rect x="0" y="0" width="4.5" height="4.5"/><rect x="6.5" y="0" width="4.5" height="4.5"/><rect x="0" y="6.5" width="4.5" height="4.5"/><rect x="6.5" y="6.5" width="4.5" height="4.5"/></svg>Financial Difficulties</li>
      <li><svg viewBox="0 0 11 11"><rect x="0" y="0" width="4.5" height="4.5"/><rect x="6.5" y="0" width="4.5" height="4.5"/><rect x="0" y="6.5" width="4.5" height="4.5"/><rect x="6.5" y="6.5" width="4.5" height="4.5"/></svg>Foreclosure or Auction</li>
      <li><svg viewBox="0 0 11 11"><rect x="0" y="0" width="4.5" height="4.5"/><rect x="6.5" y="0" width="4.5" height="4.5"/><rect x="0" y="6.5" width="4.5" height="4.5"/><rect x="6.5" y="6.5" width="4.5" height="4.5"/></svg>Quick Sale</li>
      <li><svg viewBox="0 0 11 11"><rect x="0" y="0" width="4.5" height="4.5"/><rect x="6.5" y="0" width="4.5" height="4.5"/><rect x="0" y="6.5" width="4.5" height="4.5"/><rect x="6.5" y="6.5" width="4.5" height="4.5"/></svg>Problem Renters</li>
      <li><svg viewBox="0 0 11 11"><rect x="0" y="0" width="4.5" height="4.5"/><rect x="6.5" y="0" width="4.5" height="4.5"/><rect x="0" y="6.5" width="4.5" height="4.5"/><rect x="6.5" y="6.5" width="4.5" height="4.5"/></svg>Unkept/Beat Up House</li>
    </ul>
  </section>

  <section class="bench-ad bench-ad--black">
    <div class="title-tab"></div>
    <div class="title-word">QUICK</div>
    <div class="site-band"></div>
    <div class="site-name">homebuyerdesk.com</div>
    <ul class="tagline"><li>Sell for cash</li><li>Quick closure</li><li>Any condition</li></ul>
    <div class="brand"><span class="brand-square"></span><span>QUICK HOME BUYER DESK</span></div>
    <p class="call-line"><span>Call or Text Us Now for a <span class="no-obligation">No Obligation<svg class="swoosh" viewBox="0 0 190 10"><path d="M2 8 Q95 0 188 3" fill="none" stroke-width="1.5"/></svg></span> Offer</span><span>(916) 482-3091</span></p>
    <ul class="situations">
      <li><svg viewBox="0 0 11 11"><rect x="0" y="0" width="4.5" height="4.5"/><rect x="6.5" y="0" width="4.5" height="4.5"/><rect x="0" y="6.5" width="4.5" height="4.5"/><rect x="6.5" y="6.5" width="4.5" height="4.5"/></svg>Financial Difficulties</li>
      <li><svg viewBox="0 0 11 11"><rect x="0" y="0" width="4.5" height="4.5"/><rect x="6.5" y="0" width="4.5" height="4.5"/><rect x="0" y="6.5" width="4.5" height="4.5"/><rect x="6.5" y="6.5" width="4.5" height="4.5"/></svg>Foreclosure or Auction</li>
      <li><svg viewBox="0 0 11 11"><rect x="0" y="0" width="4.5" height="4.5"/><rect x="6.5" y="0" width="4.5" height="4.5"/><rect x="0" y="6.5" width="4.5" height="4.5"/><rect x="6.5" y="6.5" width="4.5" height="4.5"/></svg>Quick Sale</li>
      <li><svg viewBox="0 0 11 11"><rect x="0" y="0" width="4.5" height="4.5"/><rect x="6.5" y="0" width="4.5" height="4.5"/><rect x="0" y="6.5" width="4.5" height="4.5"/><rect x="6.5" y="6.5" width="4.5" height="4.5"/></svg>Problem Renters</li>
      <li><svg viewBox="0 0 11 11"><rect x="0" y="0" width="4.5" height="4.5"/><rect x="6.5" y="0" width="4.5" height="4.5"/><rect x="0" y="6.5" width="4.5" height="4.5"/><rect x="6.5" y="6.5" width="4.5" height="4.5"/></svg>Unkept/Beat Up House</li>
    </ul>
  </section>

</main>
</body>
</html>
```